New Business Card Design Project

We are looking for a talented individual to create a truly awesome/unique business card design for us. We are looking for a someone to design something that will really stand out from the crowd - we don't mind what ideas you come up with (ie embossed/flat/matte/shine etc etc) just wow us with your creativity.
Updates

Target Market(s)

Video Games Industry Professionals (all levels of seniority from QA Testers through to CEOs)

Contact Information for Business Card

Company logo (see upload)
Company name: Northbay Play Careers Ltd
Employee Name: Darren Elsby
Job title: CEO
Website: www.nbpc2go.example
Office +44 1632 960418
Mobile: +44 7700 900276
Email: darren@nbpc2go.example

Colors

Designer to choose colors to be used in the design.

Requirements
Must have
• The business card design MUST contain all the information listed in the BUSINESS CARD DETAILS box.
• You will see the colours that are relevant to us (ie company logo) in the uploaded imagery - however you do not have to use all these colours when designing the business card itself
• MUST BE DOUBLE SIDED

```html
<!DOCTYPE html>
<html lang="en">
<head>
<meta charset="utf-8">
<title>Northbay Play Careers – Business Card</title>
<link rel="stylesheet" href="https://fonts.googleapis.com/css2?family=Montserrat:wght@300;400;600;700&display=swap">
<style>
  :root {
    --stage: #2b2b2e;
    --navy: #1f2d5c;
    --navy-deep: #17224a;
    --navy-soft: #33477f;
    --orange: #ee7a1f;
    --paper: #f7f7f8;
    --slate: #9aa6c8;
    --shadow: rgba(0, 0, 0, 0.45);
  }
  * { box-sizing: border-box; margin: 0; padding: 0; }
  html, body {
    width: 1200px;
    height: 900px;
    overflow: hidden;
    background: var(--stage);
    font-family: "Montserrat", sans-serif;
  }
  .stage {
    position: relative;
    width: 1200px;
    height: 900px;
  }
  .card {
    position: absolute;
    left: 270px;
    width: 660px;
    height: 377px;
    border-radius: 28px;
    overflow: hidden;
    box-shadow: 0 14px 30px var(--shadow);
  }

  /* Back side */
  .card--back {
    top: 48px;
    background: var(--navy);
  }
  .brand {
    position: absolute;
    left: 0;
    right: 0;
    top: 140px;
    display: flex;
    align-items: center;
    justify-content: center;
    gap: 16px;
  }
  .brand__mark {
    width: 44px;
    height: 44px;
    border-radius: 50%;
    background: var(--slate);
  }
  .brand__name {
    font-weight: 700;
    font-size: 34px;
    letter-spacing: 0.5px;
    color: var(--slate);
  }
  .website {
    position: absolute;
    left: 0;
    right: 0;
    top: 240px;
    text-align: center;
    font-weight: 600;
    font-size: 13px;
    letter-spacing: 3px;
    color: var(--orange);
  }

  /* Front side */
  .card--front {
    top: 470px;
    background: var(--paper);
  }
  .person {
    position: absolute;
    left: 34px;
    top: 30px;
    color: var(--navy);
  }
  .person__first {
    font-weight: 300;
    font-size: 26px;
    letter-spacing: 1px;
    line-height: 1.05;
  }
  .person__last {
    font-weight: 700;
    font-size: 22px;
    line-height: 1.15;
    padding-bottom: 4px;
    border-bottom: 2px solid var(--orange);
  }
  .person__title {
    margin-top: 5px;
    font-size: 13px;
    color: var(--orange);
    letter-spacing: 1px;
  }
  .contacts {
    position: absolute;
    left: 34px;
    bottom: 40px;
    list-style: none;
  }
  .contacts__item {
    display: flex;
    align-items: center;
    gap: 10px;
    font-size: 16px;
    color: var(--navy);
    line-height: 1.8;
  }
  .contacts__icon {
    width: 16px;
    height: 16px;
    fill: var(--orange);
    flex: none;
  }
  .illustration {
    position: absolute;
    right: 0;
    top: 0;
    width: 430px;
    height: 377px;
    background: radial-gradient(ellipse at 72% 55%, var(--navy) 0%, var(--navy-soft) 45%, rgba(51, 71, 127, 0) 72%);
  }
</style>
</head>
<body>
<main class="stage">
  <section class="card card--back" aria-label="Card back">
    <div class="brand">
      <span class="brand__mark"></span>
      <span class="brand__name">Northbay Play Careers</span>
    </div>
    <p class="website">www.nbpc2go.example</p>
  </section>

  <section class="card card--front" aria-label="Card front">
    <div class="illustration" role="img" aria-label="Navy illustration of a Viking warrior in a horned helmet with long flowing hair and beard"></div>
    <div class="person">
      <p class="person__first">DARREN</p>
      <p class="person__last">ELSBY</p>
      <p class="person__title">C.E.O.</p>
    </div>
    <ul class="contacts">
      <li class="contacts__item">
        <svg class="contacts__icon" viewBox="0 0 16 16" aria-hidden="true"><path d="M1 5c0-2 3-3 7-3s7 1 7 3v1h-3V4.5H4V6H1zM3 7h10l1 7H2zm5 1.5a2.5 2.5 0 1 0 0 5 2.5 2.5 0 0 0 0-5z"/></svg>
        +44 1632 960418
      </li>
      <li class="contacts__item">
        <svg class="contacts__icon" viewBox="0 0 16 16" aria-hidden="true"><path d="M4 0h8a1 1 0 0 1 1 1v14a1 1 0 0 1-1 1H4a1 1 0 0 1-1-1V1a1 1 0 0 1 1-1zm0.8 2v10h6.4V2zM8 13a1 1 0 1 0 0 2 1 1 0 0 0 0-2z"/></svg>
        +44 7700 900276
      </li>
      <li class="contacts__item">
        <svg class="contacts__icon" viewBox="0 0 16 16" aria-hidden="true"><path d="M0 3h16v10H0zm1.5 1.2v.3L8 9l6.5-4.5v-.3z"/></svg>
        darren@nbpc2go.example
      </li>
    </ul>
  </section>
</main>
</body>
</html>
```